creation of a business card design for a company specializing in the creation...

I would like to create a design for a professional business card on a black background and with the company's colors (I am attaching some files: including the logo in horizontal and centered format, I am also attaching a recent project design a T-shirt, this is the one I chose to give you an idea of my preferences.

we are in the process of developing a new website design, it is still in the development phase but it can be viewed at the following address: www.vendrelak.be to give you other ideas about the company
you will see for yourself the subject of my main activity: company specializing in the construction of stairs

I would like a business card that stands out from the rest with a unique design

here is the informations
Name: Florent Dubrec
Function: Manager
Address: Rue Masquelin du Pont 41
7180 Val-Saint-Orme
telephone: +32 486 219 508
email: info@rv8k.be
website: rv8k. be
social networks: Facebook, YouTube, TikTok, Instagram

Target Market(s)

customer who wants to have a beautiful staircase built

Industry/Entity Type

contruction d'escalier

Contact Information for Business Card

Adresse. Numero de telephone, site web, le texte : "Createur d'escalier", logo recto-verso, icone des reseaux sociaux

Requirements
Must have
• the mention: Stair creator
Nice to have
• an illustration of a designer staircase
Should not have
• do not distort the logo

```html
<!DOCTYPE html>
<html lang="fr">
<head>
<meta charset="utf-8">
<title>RV8K – Business card</title>
<link href="https://fonts.googleapis.com/css2?family=Poppins:wght@300;400;500&family=Oswald:wght@600&display=swap" rel="stylesheet">
<style>
  :root {
    --page: #2a2a2a;
    --card: #000000;
    --blue: #5e8fb3;
    --blue-light: #9cc0dc;
    --blue-deep: #1f4660;
    --white: #ffffff;
  }
  * { margin: 0; padding: 0; box-sizing: border-box; }
  html, body { width: 1200px; height: 1015px; overflow: hidden; }
  body {
    background: var(--page);
    font-family: "Poppins", sans-serif;
    display: flex; flex-direction: column; align-items: center; justify-content: center;
    gap: 48px;
  }
  .card {
    position: relative;
    width: 780px; height: 440px;
    background: var(--card);
    overflow: hidden;
    box-shadow: 0 12px 30px rgba(0,0,0,.5);
  }
  .card__edge {
    position: absolute; left: 0; top: 0; bottom: 0; width: 14px;
    background: var(--blue);
  }
  .card--back .card__edge { background: var(--blue-light); }

  /* Front */
  .front__brand {
    position: absolute; left: 0; right: 0; top: 140px;
    display: flex; align-items: center; justify-content: center; gap: 22px;
  }
  .brand-mark { width: 56px; height: 56px; background: var(--blue-light); }
  .brand-name {
    font-weight: 400; font-size: 92px; letter-spacing: 10px; line-height: 1;
    color: var(--white);
  }
  .socials {
    position: absolute; left: 0; right: 0; top: 300px;
    display: flex; justify-content: center; gap: 14px;
  }
  .socials span {
    width: 36px; height: 36px; border-radius: 50%;
    border: 2px solid var(--blue-light);
  }

  /* Back */
  .person { position: absolute; left: 70px; top: 70px; }
  .person__name {
    font-family: "Oswald", sans-serif; font-weight: 600; font-size: 44px;
    color: var(--blue); letter-spacing: .5px; line-height: 1;
    text-transform: uppercase;
  }
  .person__role { font-size: 26px; color: var(--white); font-weight: 400; line-height: 1.1; margin-left: 14px; }
  .person__rule { width: 64px; height: 1px; background: var(--blue); margin: 28px 0 0 30px; }
  .contact { position: absolute; left: 100px; top: 270px; }
  .contact__email { font-size: 24px; color: var(--blue-light); font-weight: 300; margin-bottom: 26px; }
  .contact__address { font-size: 24px; color: var(--white); font-weight: 300; line-height: 1.25; }

  .badge { position: absolute; left: 430px; top: 30px; width: 330px; height: 300px; }
  .badge__art {
    position: absolute; left: 50px; top: 40px; width: 230px; height: 230px; border-radius: 50%;
    background: radial-gradient(circle at 50% 45%, #8c9aa4 0%, #3d6a86 35%, var(--blue-deep) 70%, #0c1d29 100%);
  }
  .badge__title { position: absolute; left: 0; top: 0; width: 330px; height: 300px; overflow: visible; }
  .badge__title text {
    font-family: "Oswald", sans-serif; font-weight: 600; font-size: 24px;
    fill: var(--white); letter-spacing: 1px;
  }
  .badge__brand {
    position: absolute; left: 470px; top: 300px; width: 290px;
    text-align: center;
  }
  .badge__brand .brand-name { font-size: 62px; letter-spacing: 6px; }
  .badge__contact {
    display: flex; justify-content: center; gap: 14px; margin-top: 10px;
    font-size: 14px; color: var(--white); font-weight: 400;
  }
  .badge__contact span { display: inline-flex; align-items: center; gap: 5px; }
  .badge__contact svg { width: 15px; height: 15px; }
</style>
</head>
<body>

<section class="card card--front">
  <div class="card__edge"></div>
  <div class="front__brand">
    <div class="brand-mark"></div>
    <div class="brand-name">RV8K</div>
  </div>
  <div class="socials" aria-label="Réseaux sociaux">
    <span></span><span></span><span></span><span></span>
  </div>
</section>

<section class="card card--back">
  <div class="card__edge"></div>

  <div class="person">
    <div class="person__name">Florent Dubrec</div>
    <div class="person__role">Manager</div>
    <div class="person__rule"></div>
  </div>

  <div class="contact">
    <div class="contact__email">info@rv8k.be</div>
    <div class="contact__address">Rue Masquelin du Pont 41<br>7180 Val-Saint-Orme</div>
  </div>

  <div class="badge">
    <div class="badge__art" role="img" aria-label="Illustration d'un escalier design aux marches flottantes dans un cercle bleu"></div>
    <svg class="badge__title" viewBox="0 0 330 300" aria-label="Créateur d'escalier">
      <defs><path id="arc" d="M37 178 A130 130 0 0 1 255 62"/></defs>
      <text><textPath href="#arc">CRÉATEUR D'ESCALIER</textPath></text>
    </svg>
  </div>

  <div class="badge__brand">
    <div class="brand-name">RV8K</div>
    <div class="badge__contact">
      <span>
        <svg viewBox="0 0 24 24"><circle cx="12" cy="12" r="12" fill="#5e8fb3"/><path d="M8 6.5l2 2.5-1.2 1.5a8 8 0 0 0 4.7 4.7l1.5-1.2 2.5 2-1.3 1.6C12 17.6 6.4 12 6.4 7.8z" fill="#000"/></svg>
        0486 219 508
      </span>
      <span>
        <svg viewBox="0 0 24 24"><circle cx="12" cy="12" r="12" fill="#5e8fb3"/><circle cx="12" cy="12" r="6.5" fill="none" stroke="#000" stroke-width="1.5"/><path d="M5.5 12h13M12 5.5c-3 3.5-3 9.5 0 13M12 5.5c3 3.5 3 9.5 0 13" fill="none" stroke="#000" stroke-width="1.3"/></svg>
        rv8k. be
      </span>
    </div>
  </div>
</section>

</body>
</html>
```